Elegant and Professional Business card design needed

The client journey mentor is a company which provides consulting services to businesses to assist them in improving the customer experience for their customers.

I need a business card design which tells people I'm there to help them.

Target Market(s)

Small to medium business owners

Industry/Entity Type

Business

Contact Information for Business Card

Leonard Pashcroft
The Client Journey Mentor
Web: http://www.TheClientJourneyMentor.example
Email: leonard@TheClientJourneyMentor.example
Phone: +61 452 386017

Logo styles of interest
Abstract Logo
Requirements
Must have
• Some sort of image / graphic representing the customer is important and should be at the heart of a business.

```html
<!DOCTYPE html>
<html lang="en">
<head>
<meta charset="utf-8">
<title>Leonard Pashcroft – The Client Journey Mentor</title>
<link rel="stylesheet" href="https://fonts.googleapis.com/css2?family=Poppins:wght@500;600;700&display=swap">
<style>
  :root {
    --backdrop: #eef0f0;
    --card-white: #ffffff;
    --slate-grey: #a0a1a3;
    --olive-gold: #8b7526;
    --signal-red: #e21f26;
    --text-white: #ffffff;
    --icon-grey: #d9d9d9;
    --visual-light: #e4e6ea;
    --visual-mid: #9a9ea6;
  }
  html, body {
    margin: 0;
    padding: 0;
    width: 1200px;
    height: 770px;
    overflow: hidden;
    background: var(--backdrop);
  }
  .card {
    position: absolute;
    left: 69px;
    top: 82px;
    width: 1060px;
    height: 605px;
    display: block;
  }
  .card-text {
    font-family: "Poppins", "Century Gothic", sans-serif;
    fill: var(--text-white);
  }
  .holder-name { font-size: 17px; font-weight: 700; }
  .contact-line { font-size: 11.5px; font-weight: 500; }
  .company-title { font-size: 18px; font-weight: 700; letter-spacing: 0.2px; }
  .phone-number { font-size: 13px; font-weight: 600; fill: var(--signal-red); }
  .band-grey { fill: var(--slate-grey); }
  .band-olive { fill: var(--olive-gold); }
  .band-red { fill: var(--signal-red); }
  .card-base { fill: var(--card-white); }
  .line-icon { fill: none; stroke: var(--icon-grey); stroke-width: 1; }
  .phone-icon { fill: var(--signal-red); }
</style>
</head>
<body>
<svg class="card" viewBox="0 0 540 308" xmlns="http://www.w3.org/2000/svg">
  <defs>
    <linearGradient id="keyVisualTone" x1="0" y1="0" x2="1" y2="1">
      <stop offset="0" stop-color="var(--visual-light)"/>
      <stop offset="1" stop-color="var(--visual-mid)"/>
    </linearGradient>
  </defs>

  <rect class="card-base" x="0" y="0" width="540" height="308"/>
  <polygon class="band-grey" points="3,0 540,0 540,42 63,198"/>
  <polygon class="band-olive" points="0,0 3,0 96,308 0,308"/>
  <polygon class="band-red" points="540,42 540,98 78,247 63,198"/>

  <g transform="rotate(-17.7 78 113)">
    <text class="card-text holder-name" x="78" y="113">Leonard Pashcroft</text>
  </g>

  <g transform="rotate(-17.7 70 150)">
    <rect class="line-icon" x="70" y="140" width="13" height="9" rx="1"/>
    <polyline class="line-icon" points="70,140 76.5,145.5 83,140"/>
    <text class="card-text contact-line" x="88" y="149">leonard@TheClientJourneyMentor.example</text>
  </g>

  <g transform="rotate(-17.7 70 178)">
    <circle class="line-icon" cx="77" cy="173" r="6"/>
    <circle class="line-icon" cx="77" cy="173" r="3.5"/>
    <text class="card-text contact-line" x="88" y="177">www.TheClientJourneyMentor.example</text>
  </g>

  <g transform="rotate(-17.7 72 241)">
    <text class="card-text company-title" x="72" y="241">THE CLIENT JOURNEY MENTOR</text>
  </g>

  <g transform="rotate(-17.7 205 262)">
    <path class="phone-icon" d="M205 254 q-2 1 -1 4 q2 5 7 8 q3 1 4 -1 l1 -2 l-3 -2 l-2 1 q-3 -2 -4 -4 l1 -2 l-2 -3 z"/>
    <text class="card-text phone-number" x="221" y="265">+61 452 386017</text>
  </g>

  <rect x="405" y="148" width="130" height="145" rx="10" fill="url(#keyVisualTone)"
        role="img" aria-label="Illustration of a silver jigsaw puzzle piece unlocked by a golden key"/>
</svg>
</body>
</html>
```